I am a Financial Adviser specialising in Aged Care Advice. We provide financial advice and assistance to families with loved ones entering an Aged Care facility.
We need a flyer detailing the Aged Care Packages that we offer. There will be 3 main packages & then other add ons. I need an area where the client can sign off on the package/s that they choose. I have attached a sample to demonstrate the required layout, and a copy of content. I would like the flyer to have an image as per the attached sample, and to be designed in soft pastels, blues, greens.

Financial

```html
<!DOCTYPE html>
<html lang="en">
<head>
<meta charset="utf-8">
<title>Harbourline Advisory – Aged Care Packages</title>
<link href="https://fonts.googleapis.com/css2?family=Roboto+Condensed:ital,wght@0,300;0,400;0,700;1,400&display=swap" rel="stylesheet">
<style>
:root{
  --bg:#3b2c24;
  --paper:#ffffff;
  --paper-grey:#e7e8ec;
  --ink:#2b2b2b;
  --blue:#a3aacf;
  --blue-deep:#939bc5;
  --blue-tag:#8d95c3;
  --olive:#84855a;
  --olive-deep:#76774a;
  --olive-tag:#6f7044;
  --sage-light:#d4d6a8;
  --sage-band:#c3c594;
  --white:#ffffff;
}
*{box-sizing:border-box;margin:0;padding:0}
html,body{width:1200px;height:1200px;overflow:hidden}
body{background:var(--bg);font-family:"Roboto Condensed",sans-serif;color:var(--ink);position:relative}

.page{position:absolute;width:560px;height:728px;background:var(--paper);overflow:hidden;top:236px}
.page--options{left:30px}
.page--packages{left:610px}

/* ---------- Extra options page ---------- */
.options-head{position:absolute;left:0;top:0;width:100%;height:492px;background:linear-gradient(160deg,#f1f2f4 0%,var(--paper-grey) 60%,#dfe0e5 100%)}
.options-title{position:absolute;top:26px;width:100%;text-align:center;font-weight:700;font-size:29px;letter-spacing:.5px;color:#333}
.option{position:absolute;left:54px;width:478px;height:50px;background:var(--blue)}
.option--olive{background:var(--olive)}
.option__check{position:absolute;left:-23px;top:18px;width:14px;height:14px;background:#fff;border:1px solid #c8c8c8}
.option__label{position:absolute;left:0;top:0;width:148px;height:50px;background:var(--blue-deep);clip-path:polygon(0 0,88% 0,100% 50%,88% 100%,0 100%);color:#fff;text-align:center;padding-right:22px;display:flex;flex-direction:column;justify-content:center}
.option--olive .option__label{background:var(--olive-deep)}
.option__name{font-size:10.5px;font-weight:700;line-height:1.15}
.option__price{font-size:18px;font-weight:700;line-height:1.1}
.option__chevron{position:absolute;left:126px;top:0}
.option__desc{position:absolute;left:160px;right:18px;top:0;height:50px;display:flex;align-items:center;color:#fff;font-size:9.6px;font-weight:300;line-height:1.35;text-align:justify}

.agreement{position:absolute;left:31px;right:26px;top:505px;font-size:7.6px;line-height:1.4;letter-spacing:-.1px}
.sign-row{position:absolute;left:31px;right:26px;font-size:9.5px}
.sign-line{position:absolute;border-bottom:1px dotted #555;height:1px}
.sign-label{position:absolute;text-align:center}
.legal{position:absolute;left:31px;right:26px;top:638px;font-size:7.2px;line-height:1.35;letter-spacing:-.1px}
.legal p+p{margin-top:3px}
.options-foot{position:absolute;left:0;bottom:0;width:100%;height:24px;background:linear-gradient(90deg,#d9d8b8,#ebe8cf 50%,#cfcfa6)}

/* ---------- Packages page ---------- */
.hero{position:absolute;left:0;top:0;width:560px;height:278px;background:linear-gradient(180deg,#b8c98a 0%,#9fb76c 45%,#8aa558 75%,#a6b878 100%)}
.brand-panel{position:absolute;left:0;top:0;width:560px;height:278px}
.brand{position:absolute;left:36px;top:62px;display:flex;align-items:center;gap:7px;font-size:22px;font-weight:700;color:#2d2d2d}
.brand__dot{width:10px;height:10px;border-radius:50%;background:#d4a52b}
.packages-bg{position:absolute;left:0;top:274px;width:560px;height:454px;background:linear-gradient(180deg,var(--sage-light),var(--sage-band))}

.pkg{position:absolute;left:0;width:560px}
.pkg__check{position:absolute;left:24px;width:22px;height:22px;background:#fff;border:1px solid #ddd}
.pkg__label{position:absolute;left:46px;top:0;width:150px;height:100%;background:var(--olive-deep);clip-path:polygon(17% 0,100% 0,100% 100%,17% 100%,0 50%);color:#fff;padding:11px 0 0 34px}
.pkg--blue-label .pkg__label{background:var(--blue-deep)}
.pkg__title{font-size:17px;font-weight:700;line-height:1.05;letter-spacing:.3px}
.pkg__sub{font-size:16px;font-weight:700;line-height:1.1}
.pkg__price{font-size:28px;font-weight:700;margin-top:6px;line-height:1.1}
.pkg__tagline{font-size:12px;font-weight:300;line-height:1.3;margin-top:3px;padding-right:4px}
.pkg__body{position:absolute;left:196px;right:0;top:0;height:100%;background:var(--blue);color:#fff;padding:13px 0 0 11px}
.pkg--blue-label .pkg__body{background:var(--olive)}
.pkg__heading{font-size:14px;font-weight:700;margin-bottom:6px}
.pkg__list{list-style:none}
.pkg__list li{font-size:11.5px;font-weight:300;line-height:16.5px;padding-left:15px;position:relative}
.pkg__list li::before{content:"";position:absolute;left:0;top:6px;width:5px;height:5px;background:#fff}
.pkg__note{font-style:italic;font-size:13px;font-weight:400;line-height:1.3;margin:6px 0 0 15px}
.pkg__tag{position:absolute;right:0;width:144px;height:29px;border-radius:10px 0 0 10px;background:var(--blue-tag);color:#fff;font-style:italic;font-size:17px;display:flex;align-items:center;justify-content:center}
.pkg--blue-label .pkg__tag{background:var(--olive-tag)}
</style>
</head>
<body>

<section class="page page--options">
  <div class="options-head"></div>
  <h1 class="options-title">EXTRA CHOICE OPTIONS</h1>

  <div class="option" style="top:71px">
    <span class="option__check"></span>
    <div class="option__label"><span class="option__name">Centre Link / DVA Nominee</span><span class="option__price">$1,100</span></div>
    <svg class="option__chevron" width="22" height="50"><polyline points="2,0 20,25 2,50" fill="none" stroke="#fff" stroke-width="1.5"/></svg>
    <p class="option__desc">Communicate with CentreLink / DVA on behalf of our client /s, and undertake all changes and updates to details, as directed by our client.</p>
  </div>

  <div class="option option--olive" style="top:131px">
    <span class="option__check"></span>
    <div class="option__label"><span class="option__name">Post Implementation<br>Statement of Advice</span><span class="option__price">$1,650</span></div>
    <svg class="option__chevron" width="22" height="50"><polyline points="2,0 20,25 2,50" fill="none" stroke="#fff" stroke-width="1.5"/></svg>
    <p class="option__desc">Revise our original Advice Statement for any changes of circumstances including income &amp; asset variations, and provide further advice within the first 12 months of initial advice statement.</p>
  </div>

  <div class="option" style="top:191px">
    <span class="option__check"></span>
    <div class="option__label"><span class="option__name">Annual Review</span><span class="option__price">$990</span></div>
    <svg class="option__chevron" width="22" height="50"><polyline points="2,0 20,25 2,50" fill="none" stroke="#fff" stroke-width="1.5"/></svg>
    <p class="option__desc">A review of the recommendations made in our original advice document, taking into account any changes to client’s circumstances includingchecking current cash flow is sufficient to meet ongoing aged care</p>
  </div>

  <div class="option option--olive" style="top:251px">
    <span class="option__check"></span>
    <div class="option__label"><span class="option__name">Post Entry Review</span><span class="option__price">$660</span></div>
    <svg class="option__chevron" width="22" height="50"><polyline points="2,0 20,25 2,50" fill="none" stroke="#fff" stroke-width="1.5"/></svg>
    <p class="option__desc">Review financial situation, check facility invoices are accurate, explain the Residential Aged Care Agreement and ensure all recommendations are implemented.</p>
  </div>

  <div class="option" style="top:311px">
    <span class="option__check"></span>
    <div class="option__label"><span class="option__name">Facility Liason</span><span class="option__price">$550</span></div>
    <svg class="option__chevron" width="22" height="50"><polyline points="2,0 20,25 2,50" fill="none" stroke="#fff" stroke-width="1.5"/></svg>
    <p class="option__desc">Negotiate with the Aged Care Facility regarding Accommodation payments, clarify &amp; explain Residential Care Agreement, and review facility invoices.</p>
  </div>

  <div class="option option--olive" style="top:371px">
    <span class="option__check"></span>
    <div class="option__label"><span class="option__name">Family Conferences</span><span class="option__price">$660</span></div>
    <svg class="option__chevron" width="22" height="50"><polyline points="2,0 20,25 2,50" fill="none" stroke="#fff" stroke-width="1.5"/></svg>
    <p class="option__desc">Facilitate &amp; co-ordinate family meetings to explain the Aged Care legislation and how it fits with the family circumstances.</p>
  </div>

  <div class="option" style="top:431px">
    <span class="option__check"></span>
    <div class="option__label"><span class="option__name">Family Conferences</span><span class="option__price">$660</span></div>
    <svg class="option__chevron" width="22" height="50"><polyline points="2,0 20,25 2,50" fill="none" stroke="#fff" stroke-width="1.5"/></svg>
    <p class="option__desc">Facilitate &amp; co-ordinate family meetings to explain the Aged Care legislation and how it fits with the family circumstances.</p>
  </div>

  <p class="agreement">I/We have chosen the Service Package and Options as ticked above. I/We understand that by choosing the Essentials Package, that I/We are receiving factual information only, and not financial advice. I/We agree to<br>pay the amount of ……………….., within seven days of the date of the invoice received from Harbourline Advisory SA.</p>

  <div class="sign-row" style="top:556px">
    <span class="sign-line" style="left:0;width:138px;top:0"></span>
    <span class="sign-line" style="left:156px;width:128px;top:0"></span>
    <span class="sign-line" style="left:288px;width:128px;top:0"></span>
    <span class="sign-line" style="left:427px;width:72px;top:0"></span>
    <span class="sign-label" style="left:0;width:138px;top:10px">Signature</span>
    <span class="sign-label" style="left:220px;width:140px;top:10px">Signature Signature</span>
    <span class="sign-label" style="left:427px;width:72px;top:10px">Date</span>
  </div>
  <div class="sign-row" style="top:600px">
    <span class="sign-line" style="left:0;width:140px;top:0"></span>
    <span class="sign-line" style="left:153px;width:88px;top:0"></span>
    <span class="sign-label" style="left:0;width:142px;top:10px">Adviser Signature</span>
    <span class="sign-label" style="left:153px;width:88px;top:10px">Date</span>
  </div>

  <div class="legal">
    <p>This document has been prepared by Harbourline Advisory SA Pty Ltd ABN 12 345 678 901, an Authorised Representative of Meridian Wealth Limited ABN 23 456 789 012 AFSL 654321, a wholly owned, non-guaranteed subsidiary of the Southern Cross Banking Group ABN 34 567 890 123.</p>
    <p>Information in this document is based on current regulatory requirements and laws, as at 20 September, 2016 which may be subject to change. It contains general advice. It does not take into account your individual objectives, financial situation or needs. You should consider talking to a financial adviser before making a financial decision.</p>
  </div>
  <div class="options-foot"></div>
</section>

<section class="page page--packages">
  <div class="hero" role="img" aria-label="Photo of a smiling three-generation family sitting together in long summer grass"></div>
  <svg class="brand-panel" viewBox="0 0 560 278" width="560" height="278" aria-hidden="true">
    <polygon points="0,0 277,0 108,163 0,92" fill="#ffffff"/>
  </svg>
  <div class="brand"><span class="brand__dot"></span>Harbourline</div>

  <div class="packages-bg"></div>

  <div class="pkg" style="top:278px;height:138px">
    <span class="pkg__check" style="top:57px"></span>
    <div class="pkg__label">
      <div class="pkg__title">ESSENTIALS</div>
      <div class="pkg__sub">Package</div>
      <div class="pkg__price">$770</div>
      <div class="pkg__tagline">When you know<br>what you want</div>
    </div>
    <div class="pkg__body">
      <ul class="pkg__list">
        <li>Explanation of Aged Care Fees and Charges.</li>
        <li>Preliminary Home / Assets Assessment.*</li>
        <li>Estimated Means Tested Fee Calculation.*</li>
        <li>Preliminary Aged Care Costs.*</li>
        <li>Estimated Cash Flow Scenario.*</li>
      </ul>
      <p class="pkg__note">*Please note this is general factual information only.<br>We do not provide any specific personal information.</p>
    </div>
    <div class="pkg__tag" style="top:56px">Peace of Mind</div>
  </div>

  <div class="pkg pkg--blue-label" style="top:416px;height:138px">
    <span class="pkg__check" style="top:57px"></span>
    <div class="pkg__label">
      <div class="pkg__title">ADVANTAGE</div>
      <div class="pkg__sub">Package</div>
      <div class="pkg__price">$2,970</div>
      <div class="pkg__tagline">When you need to<br>know all the options</div>
    </div>
    <div class="pkg__body">
      <div class="pkg__heading">Essentials Package Plus</div>
      <ul class="pkg__list">
        <li>Analyse and Strategize Aged Care costs.</li>
        <li>Compare up to 5 Strategy options.</li>
        <li>Minimise Aged Care Costs (where possible).</li>
        <li>Maximise Age Pension Income (where possible).</li>
        <li>Prepare a Full Statement of Advice (SOA).</li>
        <li>Implementation of Aged Care Strategy.</li>
      </ul>
    </div>
    <div class="pkg__tag" style="top:55px;width:124px">Confidence</div>
  </div>

  <div class="pkg" style="top:557px;height:137px">
    <span class="pkg__check" style="top:58px"></span>
    <div class="pkg__label">
      <div class="pkg__title">PLATINUM</div>
      <div class="pkg__sub">Package</div>
      <div class="pkg__price">$5,940</div>
      <div class="pkg__tagline">When you need<br>someone to take<br>charge</div>
    </div>
    <div class="pkg__body">
      <div class="pkg__heading">Advantage Packageplus</div>
      <ul class="pkg__list">
        <li>Liase with the Aged Care Facility.</li>
        <li>CentreLink/DVA Nominee.</li>
        <li>Post Entry Review.</li>
        <li>Post Implementation SOA (if required).</li>
        <li>Annual Review.</li>
      </ul>
    </div>
    <div class="pkg__tag" style="top:55px">Convenience</div>
  </div>
</section>

</body>
</html>
```